Stationary for New Company

We need stationary designed for a new company. Details of the required stationary is attached.

The final version should be trendy, clean... only 2 colours (green + grey/black) and professional.

#1: Business Cards (design on 2 sides)
#2: Letterhead (word format)
#3: Cover Page and back cover for proposals
#4: Envelopes,
#5: Thank You card,
#6: Presentation Folder,
#7: Email signatures template (sample attached in word document)

Logo is attached. Logo can be reversed out (will attach once available). Logo can be stacked or horizontal (provided as horizontal).

Files need to be provided in ai + png format.

Target Market(s)

Business owners. More affluent.

Industry/Entity Type

Business

Requirements
Must have
• See brief

Font: Calibri
Should not have
• Photographs / stock photos

```html
<!DOCTYPE html>
<html lang="en">
<head>
<meta charset="utf-8">
<title>Northgate Brokers – Stationery Set</title>
<link rel="stylesheet" href="https://fonts.googleapis.com/css2?family=Carlito:wght@400;700&display=swap">
<style>
  :root{
    --green:#627a24;
    --green-dark:#536a1c;
    --grey:#8c8c8c;
    --grey-light:#d9d9d9;
    --ink:#333333;
    --paper:#ffffff;
    --backdrop:#ebebeb;
  }
  *{box-sizing:border-box;margin:0;padding:0}
  html,body{width:1200px;height:900px;overflow:hidden}
  body{background:var(--backdrop);font-family:"Carlito",Calibri,Arial,sans-serif;color:var(--ink);position:relative}

  .sheet{position:absolute;background:var(--paper);box-shadow:0 2px 6px rgba(0,0,0,.12);overflow:hidden}

  .brand{display:flex;align-items:center;gap:6px;color:var(--green);font-weight:700;white-space:nowrap}
  .brand-mark{display:block;background:var(--green)}
  .brand--sm{font-size:15px}.brand--sm .brand-mark{width:14px;height:14px}
  .brand--md{font-size:22px}.brand--md .brand-mark{width:20px;height:20px}
  .brand--lg{font-size:28px}.brand--lg .brand-mark{width:26px;height:26px}

  .accent-rule{position:absolute;height:4px;background:var(--green)}
  .accent-rule::before{content:"";position:absolute;right:100%;top:0;width:10px;height:4px;background:var(--grey);margin-right:3px}

  /* Letterhead */
  .letterhead{left:40px;top:40px;width:360px;height:509px;padding:40px 34px}
  .letterhead .brand{margin-bottom:38px}
  .letter-salutation{font-weight:700;font-size:10px;margin-bottom:8px}
  .letter-body p{font-size:7.5px;line-height:1.55;color:#555;margin-bottom:8px}
  .letter-signoff{font-size:7.5px;color:#555;margin-top:12px}
  .letter-signer{font-size:9px;font-weight:700;color:var(--ink);margin-top:22px}
  .letterhead .accent-rule{left:140px;right:0;bottom:62px}
  .letter-web{position:absolute;right:34px;bottom:72px;font-size:7px;color:var(--grey)}
  .letter-footer{position:absolute;left:34px;bottom:36px;font-size:7px;color:var(--grey)}

  /* Presentation folder */
  .folder{left:430px;top:40px;width:400px;height:310px}
  .folder .brand{position:absolute;left:36px;top:34px}
  .folder-panel{position:absolute;left:0;right:0;bottom:0;height:200px;background:var(--green)}
  .folder-stripe{position:absolute;left:0;right:0;bottom:206px;height:4px;background:var(--green)}
  .folder-stripe::before{content:"";position:absolute;left:0;top:0;width:90px;height:4px;background:var(--grey)}

  /* Envelope */
  .envelope{left:860px;top:40px;width:300px;height:150px}
  .envelope-flap{position:absolute;left:0;right:0;top:0;height:52px;background:var(--green);border-radius:0 0 14px 0}

  /* Compliment slip / DL sheet */
  .slip{left:860px;top:215px;width:300px;height:170px}
  .slip .brand{position:absolute;left:24px;top:60px}
  .slip .accent-rule{left:80px;right:0;bottom:38px}
  .slip-address{position:absolute;left:24px;bottom:18px;font-size:7px;color:var(--grey)}

  /* Business cards */
  .card{width:210px;height:120px}
  .card-front{left:430px;top:385px}
  .card-front .brand{position:absolute;left:50%;top:50%;transform:translate(-50%,-50%)}
  .card-front .accent-rule,.card-back .accent-rule{left:70px;right:0;bottom:14px}
  .card-back{left:430px;top:525px;padding:18px 16px}
  .card-name{font-size:11px;font-weight:700;color:var(--green)}
  .card-role{font-size:8px;color:var(--grey);margin-bottom:10px}
  .card-details{font-size:7.5px;line-height:1.5;color:#555}
  .card-details b{color:var(--green)}
  .card-back .brand{position:absolute;right:16px;top:18px}

  /* Notebook */
  .notebook{left:680px;top:420px;width:230px;height:320px;border-left:8px solid #444}
  .notebook .brand{position:absolute;left:26px;top:36px}
  .notebook-panel{position:absolute;left:0;right:0;bottom:0;height:190px;background:var(--green)}
  .notebook-stripe{position:absolute;left:0;right:0;bottom:196px;height:4px;background:var(--green)}
  .notebook-stripe::before{content:"";position:absolute;left:0;top:0;width:50px;height:4px;background:var(--grey)}
</style>
</head>
<body>

  <article class="sheet letterhead">
    <div class="brand brand--md"><span class="brand-mark"></span>Northgate Brokers</div>
    <p class="letter-salutation">Dear sir / madame,</p>
    <div class="letter-body">
      <p>Thank you for choosing us to review your cover. We have compared policies from leading insurers and prepared options that suit your business, your budget and the way you work. Each option is explained plainly so you can decide with confidence.</p>
      <p>Please call us if you would like to talk through any detail. We look forward to working with you.</p>
    </div>
    <p class="letter-signoff">Yours Sincerely,</p>
    <p class="letter-signer">Clara Dunn</p>
    <span class="letter-web">www.northgatebrokers.com</span>
    <div class="accent-rule"></div>
    <p class="letter-footer">14 Market Row, Kingsford NS 2204 &nbsp;|&nbsp; Phone: 02 5550 1842</p>
  </article>

  <section class="sheet folder">
    <div class="brand brand--lg"><span class="brand-mark"></span>Northgate Brokers</div>
    <div class="folder-stripe"></div>
    <div class="folder-panel"></div>
  </section>

  <section class="sheet envelope">
    <div class="envelope-flap"></div>
  </section>

  <section class="sheet slip">
    <div class="brand brand--md"><span class="brand-mark"></span>Northgate Brokers</div>
    <div class="accent-rule"></div>
    <p class="slip-address">14 Market Row, Kingsford NS 2204</p>
  </section>

  <section class="sheet card card-front">
    <div class="brand brand--sm"><span class="brand-mark"></span>Northgate Brokers</div>
    <div class="accent-rule"></div>
  </section>

  <section class="sheet card card-back">
    <p class="card-name">LEON MARSH</p>
    <p class="card-role">Account Manager</p>
    <p class="card-details"><b>Phone:</b> 02 5550 1842<br><b>Email:</b> leon@northgatebrokers.com<br><b>Web:</b> northgatebrokers.com</p>
    <div class="brand brand--sm"><span class="brand-mark"></span>Northgate</div>
    <div class="accent-rule"></div>
  </section>

  <section class="sheet notebook">
    <div class="brand brand--md"><span class="brand-mark"></span>Northgate Brokers</div>
    <div class="notebook-stripe"></div>
    <div class="notebook-panel"></div>
  </section>

</body>
</html>
```